Verostel business card

Business card for sustainable investment company called "Verostel". Verostel is an exchange platform selling carbon credits between buyers and sellers. Carbon Credits are an environmental commodity for reducing global carbon emissions.

the card should obviously have our logo and the theme should be sustainability/environment mixed with a trading platform.

Contact Information for Business Card

Logo, Name, Title, Phone, Email

Colors
0054AA
0677BA
7BADD7
CADEEF
E8F1F8
0094D4
00A9DD
6FCCEA
C7EBF8
E9F6FB
00AB8E
00BBA5
67D7C9
C6EFE9
E9F9F6
59FF00
82FF00
B8FF75
E3FFCB
F4FFEA

```html
<!DOCTYPE html>
<html lang="en">
<head>
<meta charset="UTF-8">
<title>Verostel Business Card</title>
<link href="https://fonts.googleapis.com/css2?family=Raleway:wght@700&family=Montserrat:wght@400;500&family=Pinyon+Script&display=swap" rel="stylesheet">
<style>
  :root {
    --backdrop: #d3d4d6;
    --card-white: #ffffff;
    --navy: #16295a;
    --teal-light: #67c9d9;
    --blue-mid: #5aa3d2;
    --blue-deep: #4a7cc3;
    --divider: #5aa3d2;
  }
  * { margin: 0; padding: 0; box-sizing: border-box; }
  html, body {
    width: 900px;
    height: 1200px;
    overflow: hidden;
    background: var(--backdrop);
  }
  .card {
    position: absolute;
    left: 90px;
    width: 720px;
  }
  .card-front {
    top: 152px;
    height: 407px;
    background: linear-gradient(90deg, var(--teal-light) 0%, var(--blue-mid) 60%, var(--blue-deep) 100%);
  }
  .front-brand {
    position: absolute;
    left: 0;
    right: 0;
    top: 174px;
    display: flex;
    align-items: center;
    justify-content: center;
    gap: 18px;
  }
  .brand-dot {
    width: 50px;
    height: 50px;
    border-radius: 50%;
    background: var(--card-white);
  }
  .front-name {
    font-family: "Raleway", sans-serif;
    font-weight: 700;
    font-size: 58px;
    line-height: 1;
    color: var(--card-white);
    letter-spacing: 1px;
  }
  .card-back {
    top: 615px;
    height: 433px;
    background: var(--card-white);
    text-align: center;
  }
  .back-dot {
    position: absolute;
    left: 327px;
    top: 48px;
    width: 66px;
    height: 66px;
    border-radius: 50%;
    background: var(--blue-mid);
  }
  .back-name {
    position: absolute;
    left: 0;
    right: 0;
    top: 132px;
    font-family: "Raleway", sans-serif;
    font-weight: 700;
    font-size: 54px;
    line-height: 1;
    color: var(--navy);
    letter-spacing: 1px;
  }
  .person-name {
    position: absolute;
    left: 0;
    right: 0;
    top: 251px;
    font-family: "Raleway", sans-serif;
    font-weight: 700;
    font-size: 32px;
    line-height: 1;
    letter-spacing: 0.5px;
    background: linear-gradient(90deg, var(--teal-light), var(--blue-deep));
    -webkit-background-clip: text;
    background-clip: text;
    color: transparent;
    width: max-content;
    margin: 0 auto;
  }
  .person-title {
    position: absolute;
    left: 0;
    right: 0;
    top: 286px;
    font-family: "Pinyon Script", cursive;
    font-size: 21px;
    line-height: 1;
    color: var(--navy);
  }
  .contact-line {
    position: absolute;
    left: 0;
    right: 0;
    top: 325px;
    display: flex;
    justify-content: center;
    align-items: center;
    gap: 14px;
    font-family: "Montserrat", sans-serif;
    font-weight: 400;
    color: var(--navy);
    line-height: 1;
  }
  .contact-web { font-size: 17px; letter-spacing: 3px; }
  .contact-phone { font-size: 19px; letter-spacing: 5px; }
  .contact-divider {
    width: 2px;
    height: 24px;
    background: var(--divider);
  }
  .contact-email {
    position: absolute;
    left: 0;
    right: 0;
    top: 366px;
    font-family: "Montserrat", sans-serif;
    font-weight: 400;
    font-size: 16px;
    letter-spacing: 3.5px;
    color: var(--navy);
    line-height: 1;
  }
</style>
</head>
<body>
  <section class="card card-front">
    <div class="front-brand">
      <span class="brand-dot"></span>
      <span class="front-name">VEROSTEL</span>
    </div>
  </section>

  <section class="card card-back">
    <span class="back-dot"></span>
    <h1 class="back-name">VEROSTEL</h1>
    <h2 class="person-name">MARCUS HALE</h2>
    <p class="person-title">Founder</p>
    <p class="contact-line">
      <span class="contact-web">WWW.VEROSTEL.COM</span>
      <span class="contact-divider"></span>
      <span class="contact-phone">303-555-0147</span>
    </p>
    <p class="contact-email">INFO@VEROSTEL.COM</p>
  </section>
</body>
</html>
```